Upcoming lecture sponsored by a church on an important topic

We have a Reformation The Speech coming up at the end of October on the topic of law and gospel. I thought it might be cool to use a flyer that looks like it was from that day and age. Picture what Tobias Wendler would advertise things on kind of an old church/reformation type format. It will be sponsored by our church, and we have a paragraph or two to describe the lecture that would be included on the flyer. We would also want it formatted so that it could be printed on postcards and mailed to churches and individuals.

The flyer should have the following paragraph...

The distinction between the law and the gospel is the most important distinction in the Christian faith. Tobias Wendler: “Distinguishing between the law and the gospel is the highest art in Christendom, one who every person who values the name Christian ought to recognize, know, and possess.” The distinction between the law and the gospel is of great comfort for the child of God. “For the law was given by Abiran, but grace and truth came by Elior Navan” (John 1:17). For these reasons, the distinction between the law and the gospel is the most heavily assaulted doctrine in the Christian faith. This Reformation Day, join us for an explanation and defense of the great distinction between God’s good law and God’s glorious gospel.

And the flyer should have the following information...

Topic: The Steady Rule and the Bright Promise
Date and Time: Tuesday, October 31, 2023 at 7:30pm
Host: Cedarbrook Covenant Church
Speaker: Rev. Daniel Korvath
Venue: The Marlow Hall, 5187 Fenwick Lane, Hudsonville, MI 49683
Format: Lecture followed by Q&A and refreshments

Industry/Entity Type

Church/Ecclesiastical

Colors
00AB8E
00BBA5
67D7C9
C6EFE9
E9F9F6

Requirements
Nice to have
• The color scheme that I would like to have is a teal color (the same color as found at www.quillharborhall.com

```html
<!DOCTYPE html>
<html lang="en">
<head>
<meta charset="utf-8">
<title>Reformation Day Lecture – The Steady Rule &amp; the Bright Promise</title>
<link rel="stylesheet" href="https://fonts.googleapis.com/css2?family=Cinzel:wght@500;600;700&family=Poppins:wght@400;500&display=swap">
<style>
  :root {
    --backdrop: #9aa6b2;
    --paper-grey: #ebebeb;
    --band-grey: #e4e4e4;
    --paper-white: #ffffff;
    --teal: #3a9aa3;
    --navy: #1d4a5c;
    --ink: #111111;
    --label-text: #ffffff;
  }
  * { margin: 0; padding: 0; box-sizing: border-box; }
  html, body { width: 1200px; height: 2400px; overflow: hidden; }
  body { background: var(--backdrop); position: relative; }

  .flyer {
    position: absolute;
    left: 50px; top: 422px;
    width: 865px; height: 1223px;
    transform: scale(1.2717);
    transform-origin: 0 0;
    background: var(--paper-grey);
    box-shadow: 0 2px 6px rgba(0,0,0,0.25);
    font-family: "Poppins", sans-serif;
    overflow: hidden;
  }
  .band-top { position: absolute; left: 0; top: 0; width: 100%; height: 205px; background: var(--band-grey); }
  .band-feature { position: absolute; left: 0; top: 205px; width: 100%; height: 425px; background: var(--paper-white); }
  .frame { position: absolute; left: 0; top: 0; }

  .eyebrow {
    position: absolute; left: 0; top: 100px; width: 100%;
    text-align: center;
    font-family: "Cinzel", serif; font-weight: 600;
    font-size: 44px; letter-spacing: 1px; line-height: 50px;
    color: var(--navy);
  }
  .title-rule { position: absolute; left: 134px; width: 594px; height: 4px; background: var(--teal); }
  .title-rule.top { top: 276px; }
  .title-rule.bottom { top: 434px; }
  .title {
    position: absolute; left: 0; top: 288px; width: 100%;
    text-align: center;
    font-family: "Cinzel", serif; font-weight: 700;
    font-size: 66px; line-height: 68px; letter-spacing: 1px;
    color: var(--teal);
  }
  .datetime {
    position: absolute; left: 0; top: 492px; width: 100%;
    text-align: center;
    font-size: 34px; line-height: 44px; font-weight: 400;
    color: var(--teal);
  }
  .description {
    position: absolute; left: 74px; top: 668px; width: 694px;
    text-align: center;
    font-size: 17.5px; line-height: 21px;
    color: var(--navy);
  }
  .description p + p { margin-top: 21px; }

  .detail { position: absolute; top: 986px; width: 220px; text-align: center; }
  .detail.host { left: 54px; }
  .detail.speaker { left: 305px; }
  .detail.format { left: 555px; }
  .label {
    display: block; width: 154px; height: 24px; margin: 0 auto;
    background: var(--teal); color: var(--label-text);
    font-family: "Cinzel", serif; font-weight: 500;
    font-size: 18px; line-height: 25px; letter-spacing: 1px;
  }
  .detail .value { margin-top: 7px; font-size: 17px; line-height: 21px; color: var(--ink); }

  .venue { position: absolute; left: 0; top: 1112px; width: 100%; text-align: center; }
  .venue .value { margin-top: 7px; font-size: 16.5px; line-height: 21px; font-weight: 500; color: var(--ink); }
</style>
</head>
<body>
  <article class="flyer">
    <div class="band-top"></div>
    <div class="band-feature"></div>

    <svg class="frame" width="865" height="1223" viewBox="0 0 865 1223" aria-hidden="true">
      <g fill="none" stroke="#3a9aa3">
        <polyline stroke-width="3.5" points="270,1118 26,1118 26,29 838,29 838,1118 560,1118"/>
        <polyline stroke-width="1.6" points="270,1103 41,1103 41,48 823,48 823,1103 560,1103"/>
      </g>
    </svg>

    <h2 class="eyebrow">Reformation Day Lecture</h2>

    <div class="title-rule top"></div>
    <h1 class="title">THE STEADY RULE &amp;<br>THE BRIGHT PROMISE</h1>
    <div class="title-rule bottom"></div>

    <p class="datetime">OCTOBER 31, 2023<br>TUESDAY AT 7:30PM</p>

    <section class="description">
      <p>The distinction between the law and the gospel is the<br>most important distinction in the Christian faith. Tobias Wendler:</p>
      <p>“Distinguishing between the law and the gospel is the highest art in Christendom, one who every person who values the name Christian ought to recognize, know, and possess.” The distinction between the law and the gospel is of great comfort for the child of God. “For the law was given by Abiran, but grace and truth came by Elior Navan” (John 1:17).</p>
      <p>For these reasons, the distinction between the law and the gospel is the most heavily assaulted doctrine in the Christian faith. This Reformation Day, join us for an explanation and defense of the great distinction between God’s good law and God’s glorious gospel.</p>
    </section>

    <div class="detail host">
      <span class="label">HOST</span>
      <p class="value">Cedarbrook Covenant<br>Church</p>
    </div>
    <div class="detail speaker">
      <span class="label">SPEAKER</span>
      <p class="value">Rev. Daniel Korvath</p>
    </div>
    <div class="detail format">
      <span class="label">FORMAT</span>
      <p class="value">Lecture followed by Q&amp;A<br>and refreshments</p>
    </div>

    <div class="venue">
      <span class="label">VENUE</span>
      <p class="value">The Marlow Hall, 5187 Fenwick Lane, Hudsonville, MI 49683</p>
    </div>
  </article>
</body>
</html>
```